GULL REEF DISTILLERY BOTTLE LABELS

Hello Designers,

I would like to see the bottles literally be labeled as an absolute stand out from any competitor, incorporating eye-catching copper colour label background colour which matches the colour of my two Copper Pot Stills.

Front Label will be black font on copper label
saying:-

Gull Reef Distillery

A "mm♡" water mark to be incorporated on main label (example attached)

Plus an outline of Gull Reef, (located in Tasmania, Australia), suttle and cleverly included, but only to those who are particularly observant.

I also have visualised Angel wings in a copper outline with diamond details (photo of my necklace attached), incorporated with the two 55L copper stills (photo attached).

I have taken a photo of the Velvet Heron Stills (as attached file ‘outline') and have done my best to edit it to show that I would just like the outline to be shown for the copper coloured label (no hoses or shadows should be in it).

Naturally, there are other labels needed to compliment the main Label on the bottle of spirit. For reference much of the rest of the standard information will be very similar to labels on other bottles in any bottle shop.

The Gull Reef Distillery label separate to the Main Brand logo will be a different colour background & font

a Front) Gin Spirit Label)) - Blue colour font
Title = Gull Reef Native Gin
_______ ml - Crafted to enjoy now
%Alc Vol _______ Standard Drinks ________

b Front Label) Vodka Spirit Label )) - Ruby colour font
Title = Gull Reef Ruby Vodka
Crafted to enjoy now
____ ml ____%Alc Vol ____ Standard Drinks

c Front label) Whisky Single Malt Spirit Label )) - Green colour font
Title = T42 Single Malt Whisky
Crafted and aged ready to enjoy now
Bottle # _______ Cask # & Type __________

a + b back Label) Information Label (for Gin & Vodka Bottles))

Spirit distilled by Marta Drovely in Velvet Heron Stills
Bottled at Gull Reef Distillery
Currie, Gull Reef, Tasmania
Product of Australia (maybe use logo instead of text)
You'll find more Gull Reef made Product and Gifts at
www.gullreefdistillery.example
Mobile: 0477 SALUTE

c Back label) Whisky Single Malt Spirit Label
Distilled at: Brambleford Distillery
Western Junction, Tasmania
Bottled by Marta Drovely
Gull Reef Distillery
Product of Australia
Mobile: 0477 SALUTE

e Back label) Information label for all bottles and spirits
Recycle logo (Australian Standard)
Don't Drink While Pregnant Logo in Colour (details attached)
Blank white Angel Wings Shape shape Section (section for me to personally dedicate bottle by hand written signature)

3rd Section) mm❤ short & sweet story (yet to be finalised out of some of the info given below)

A bit more elaboration about this Project: My story is that I was made on Gull Reef and I love living a life of freedom, walking daily on our bare beaches and taking photos of this amazing unique place and always able to find a smiling and supportive face. I am very passionate about our Island, all that is has to offer including our world class quality produce, the outstanding quality brand that we are well known for by everyone and the friendly locals.

A native Lady is very exciting to be running the 1st Distillery at 40 degrees South. Making Spirits on Gull Reef in Bass Strait Tasmania, well known as the Roaring 40's. It is known to have the freshest / purest air in the world and likewise with rain water, it sure seems that was to us anyway. Also famous for the tallest lighthouse in the Southern Hemisphere built because of the large number of shipwrecks around Gull Reef, especially the Cataraqui.

My mission is to contribute more to our local economy and community and do this Island and our Industry proud, by way of building and operating a profitable first class boutique spirit distillery that can grow with demand. Using our local products and botanicals to make our very own beautiful beverages to be enjoyed by my Family, residents, visitors and those from afar.

After 7 years in design, now distilling with 2 custom made Copper 55L Pot Stills, namely my Copper Herons, that travelled across wild seas on a Cray Boat to their new home and are now making award winning spirits.
Namely Gin, using Gull Reef coastal and beachside botanicals, also Ruby Grapefruit & Ginger Vodka. In addition I will also be releasing T42 Single Malt Whisky.

To follow will be other varieties made with Local Produce such as Gull Reef apple and Gull Reef honey spirits and this range will grow with demand.

The growing Industry as I know it, the Distillers and their Teams are fun, friendly with passion and professionalism about awesome alcoholic beverages.

Gull Reef Distillery Sales will be aimed predominantly people visiting the Island. Our market is predominately Golfers, as Gull Reef has two very highly ranked Public Links Courses in Australia and the World. Websites and Podcast still to be developed will which build relationships with current and new people, share our entertaining distilling journey and provide educational information about our Industry and surrounds that make our product such great quality with the naturally amazing wild yeasts and so on.

Gull Reef Distillery will also be selling bottles online and posting orders from Gull Reef to Australia, whereby we want our final design be a simple, effective and consistent brand that shines of natural outstanding qualities of our spirits. Creating an exciting and unforgettable unboxing experience to keep our customers coming back to buy more bottles of spirits from Gull Reef Distillery.

The logo chosen will set us apart from the rest making Gull Reef Distillery easily recognisable and people will respond with a smile and buy bottles. They will be compelled to proudly share the news of their purchase and details of the Distillery far and wide on a variety of Media platforms and consistently returning for more of our delicious Products.

Bottles of Spirit made by Gull Reef Distillery will also be the new gift to give both males and females, plus a great present to give to those celebrating any occasion.
Customers will be given the opportunity for the bottle to be dedicated as a one of a kind for themselves of as a gift, hand-signed with a personalised note to the person from Merry Marta | Gull Reef Distillery.

Furthermore a series of unique hand made small batch collectables will be next in design…..

Bottles details at this stage are…. (but subject to change)

200ML & 700ML OSLO STYLE BOTTLES MARCH 2020 BOTTLES AT GR DISTILLERY
http://www.vesselmart.example/p7724qrt.html

700ml size are to be served behind bars and in restaurants
200ml make the perfect gift and travel size.
Will also be selling 200ml in gift packs of 3 in a black Jute bag with cane handles and a see through face.
Thank you so much, happy to discuss further to help with design finalisation.
mm❤
MARTA

Hello, My Sincere apologies that I have not responded sooner. Thank you all for your patience.

Target Market(s)

Golfers, award winning hand-made Spirit appreciators and collectors

Font styles to use
Other font styles liked:
• Feeling Lovely has been used previously for the mm❤

Requirements
Must have
• Stand out
Copper Background on Main Label
Nice to have
• Please see in Project description what I think would be nice. Also attached files help to visualise what I have in mind.
Should not have
• I wouldn't tell a great designer what not to do :-)

```html
<!DOCTYPE html>
<html lang="en">
<head>
<meta charset="utf-8">
<title>Gull Reef Native Gin Labels</title>
<link rel="stylesheet" href="https://fonts.googleapis.com/css2?family=Cinzel:wght@600;700;800&family=Crimson+Text&family=Dancing+Script:wght@500&display=swap">
<style>
  :root {
    --backdrop: #b5d3d6;
    --copper: #d9834a;
    --copper-deep: #b8622e;
    --label-black: #2a2b2d;
    --gin-blue: #36a9e1;
    --ink: #1e1e1e;
  }
  html, body {
    margin: 0;
    padding: 0;
    width: 1200px;
    height: 1142px;
    overflow: hidden;
    background: var(--backdrop);
  }
  .canvas {
    position: relative;
    width: 1200px;
    height: 1142px;
  }
  .brand-label {
    position: absolute;
    left: 419px;
    top: 184px;
    width: 377px;
    height: 263px;
    border-radius: 50%;
    background: radial-gradient(ellipse at 50% 40%, var(--copper) 0%, var(--copper-deep) 100%);
    display: flex;
    align-items: center;
    justify-content: center;
  }
  .brand-name {
    font-family: "Cinzel", serif;
    font-weight: 700;
    font-size: 26px;
    color: var(--ink);
    text-align: center;
    line-height: 1.25;
    letter-spacing: 1px;
  }
  .gin-label {
    position: absolute;
    left: 316px;
    top: 500px;
    width: 584px;
    height: 383px;
    background: var(--label-black);
    overflow: hidden;
  }
  .side-copy {
    position: absolute;
    top: 36px;
    width: 150px;
    font-family: "Crimson Text", serif;
    font-size: 18px;
    line-height: 27.5px;
    color: var(--gin-blue);
    opacity: 0.85;
    white-space: nowrap;
  }
  .side-copy.left { left: -82px; text-align: right; width: 130px; }
  .side-copy.right { left: 520px; }
  .frame {
    position: absolute;
    left: 93px;
    top: 58px;
  }
  .title-box {
    position: absolute;
    left: 158px;
    top: 35px;
    width: 261px;
    height: 55px;
    box-sizing: border-box;
    border: 2px solid var(--gin-blue);
    background: var(--label-black);
    display: flex;
    align-items: center;
    justify-content: center;
    font-family: "Cinzel", serif;
    font-weight: 800;
    font-size: 29px;
    color: var(--gin-blue);
  }
  .variety {
    position: absolute;
    left: 0;
    width: 584px;
    top: 108px;
    text-align: center;
    font-family: "Cinzel", serif;
    font-weight: 700;
    font-size: 42px;
    letter-spacing: 8px;
    color: var(--gin-blue);
  }
  .variety .rule {
    display: inline-block;
    width: 28px;
    height: 2px;
    background: var(--gin-blue);
    vertical-align: middle;
    margin: 0 6px;
  }
  .spirit {
    position: absolute;
    left: 0;
    width: 584px;
    top: 150px;
    text-align: center;
    font-family: "Cinzel", serif;
    font-weight: 700;
    font-size: 136px;
    line-height: 1.1;
    color: var(--gin-blue);
  }
  .volume {
    position: absolute;
    left: 0;
    width: 584px;
    top: 305px;
    text-align: center;
    font-family: "Dancing Script", cursive;
    font-size: 21px;
    color: var(--gin-blue);
  }
  .strength {
    position: absolute;
    left: 0;
    width: 584px;
    top: 343px;
    text-align: center;
    font-family: "Cinzel", serif;
    font-weight: 700;
    font-size: 15px;
    color: var(--gin-blue);
  }
</style>
</head>
<body>
<main class="canvas">
  <section class="brand-label">
    <div class="brand-name">Gull Reef<br>Distillery</div>
  </section>

  <section class="gin-label">
    <p class="side-copy left">ipsum<br>it amet,<br>etur ad-<br>elit,<br>eiusmod<br>incidi-<br>labore<br>e magna<br>Quis<br>uspen-</p>
    <p class="side-copy right">Lorem ipsum<br>dolor sit amet,<br>consectetur ad-<br>ipiscing elit,<br>sed do eiusmod<br>tempor inci-<br>dunt ut labore<br>et dolore magna<br>aliqua. Quis<br>ipsum suspen-</p>

    <svg class="frame" width="396" height="232" viewBox="0 0 396 232" aria-hidden="true">
      <g fill="none" stroke="var(--gin-blue)" stroke-width="2">
        <path d="M12 2 H384 V12 H394 V220 H384 V230 H12 V220 H2 V12 H12 Z"/>
        <path d="M17 9 H379 V17 H387 V215 H379 V223 H17 V215 H9 V17 H17 Z"/>
      </g>
    </svg>

    <div class="title-box">Gull Reef</div>
    <div class="variety"><span class="rule"></span>Native<span class="rule"></span></div>
    <div class="spirit">Gin</div>
    <div class="volume">700 ml - Crafted to enjoy now</div>
    <div class="strength">40%Alc Vol</div>
  </section>
</main>
</body>
</html>
```